I am looking to create a newly designed website for our national leadership conference which is entitled, "The Lantern Path Leadership Summit". The Lantern Path Leadership Summit is a national conference for student leaders that prepares them for career leadership success. The current website can be seen at www.lanternpathleadershipsummit.com.

My goal for the new site is to create a more updated, fresh, hip, and exciting look that appeals to the younger generation while also maintaining are professional appeal. The color should be black, white, and gold. We want there to be live videos played and places to insert pictures for the panels as well.

I look forward to seeing you the new creations.

Number of Pages Required

1 page

Requirements
Must have
• Ability to play videos on the home page and throughout the website. Also, make sure that the website shows up clearly on an iPhone.
Nice to have
• Nice look

```html
<!DOCTYPE html>
<html lang="en">
<head>
<meta charset="utf-8">
<title>The Lantern Path Leadership Summit – Registration</title>
<link href="https://fonts.googleapis.com/css2?family=Roboto:wght@300;400;500;700&display=swap" rel="stylesheet">
<style>
:root{
  --gold:#b98f3e;
  --gold-light:#d2ab5d;
  --dark:#222222;
  --darker:#1a1a1a;
  --grey-band:#f1f1f1;
  --text:#3a3a3a;
  --muted:#8a8a8a;
  --white:#ffffff;
}
*{box-sizing:border-box;margin:0;padding:0}
html,body{width:1200px;height:2671px;overflow:hidden}
body{font-family:'Roboto',Arial,sans-serif;color:var(--text);background:var(--white);position:relative}
.gold{color:var(--gold)}
.site-header{height:125px;position:relative}
.follow{position:absolute;left:75px;top:48px;display:flex;align-items:center;gap:5px;font-size:12px;font-weight:500;color:#222}
.follow span{margin-right:6px}
.social{width:26px;height:26px;background:#555;display:inline-block}
.brand{position:absolute;left:0;right:0;top:22px;text-align:center}
.brand-mark{width:34px;height:34px;border-radius:50%;background:var(--gold);margin:0 auto 6px}
.brand-name{font-size:17px;font-weight:700;letter-spacing:1px;color:#222;text-transform:uppercase}
.btn-gold{display:inline-block;background:linear-gradient(var(--gold-light),var(--gold));color:#fff;border-radius:40px;text-transform:uppercase;text-align:center;font-weight:500}
.header-cta{position:absolute;left:904px;top:34px;width:221px;height:51px;line-height:51px;font-size:22px}
.main-nav{height:60px;background:linear-gradient(#3a3a3a,#111);display:flex;justify-content:center;gap:0}
.main-nav a{color:#fff;text-decoration:none;font-size:14px;line-height:60px;padding:0 23px;text-transform:uppercase}
.main-nav a.active{background:var(--gold);padding:0 22px}
.breadcrumb{height:68px;padding:34px 0 0 83px;font-size:12px;text-transform:uppercase;color:#555}
.breadcrumb b{color:var(--gold);font-weight:400}
.logo-band{height:130px;background:var(--grey-band);display:flex;align-items:center;padding:0 0 0 78px}
.band-title{display:flex;align-items:center;gap:14px;width:300px;font-size:24px;line-height:28px;text-transform:uppercase;color:#222}
.dot{width:44px;height:44px;border-radius:50%;background:var(--gold);flex:none}
.carousel{display:flex;align-items:center;gap:0;flex:1;padding-right:60px}
.arrow{width:22px;font-size:28px;color:#222;text-align:center}
.carousel .items{flex:1;display:flex;justify-content:space-around;align-items:center}
.partner{font-size:20px;font-weight:700;color:#444}
.badge{width:80px;height:92px;border-radius:50%;background:#c8c8c8}
.section-title{display:flex;align-items:center;justify-content:center;gap:14px;font-size:24px;text-transform:uppercase;color:#222}
.section-title .dot{width:48px;height:40px}
.registration{height:450px;position:relative}
.registration .section-title{position:absolute;top:50px;left:0;right:0}
.reg-text{position:absolute;left:75px;top:115px;width:585px;font-size:14px;line-height:23px;color:#444;font-weight:300}
.reg-text p{margin-bottom:12px}
.photo{background:linear-gradient(135deg,#6f6a6c,#3b3638 60%,#8d8588)}
.reg-photo{position:absolute;left:696px;top:121px;width:429px;height:285px}
.roles{height:413px;background:var(--gold);display:flex;justify-content:center;padding-top:43px}
.role{width:270px;text-align:center;color:#fff}
.role-icon{width:110px;height:110px;border-radius:50%;background:#fff;margin:0 auto 30px;display:flex;align-items:center;justify-content:center}
.role h3{font-size:18px;font-weight:500;margin-bottom:12px}
.role p{font-size:14px;line-height:23px;color:#f3e3c3;font-weight:300;padding:0 18px}
.btn-dark{display:inline-block;margin-top:30px;width:128px;height:37px;line-height:37px;border-radius:20px;background:linear-gradient(#3a3a3a,#111);color:#fff;font-size:13px;font-weight:500}
.logo-band.schools{height:134px}
.schools .items{justify-content:space-between;padding:0 12px}
.register-cta{height:325px;position:relative}
.cta-photo{position:absolute;left:75px;top:40px;width:358px;height:239px;background:linear-gradient(160deg,#e9e9e9,#8c8c8c 60%,#444)}
.cta-btn{position:absolute;left:468px;top:60px;width:332px;height:64px;line-height:64px;font-size:27px}
.cta-text{position:absolute;left:473px;top:148px;width:650px;font-size:16px;line-height:27px;color:#333}
.pricing{position:absolute;left:75px;top:1705px;width:1050px;height:412px;background:var(--dark);border-radius:32px}
.pricing .section-title{color:#fff;margin-top:32px}
.cards{display:flex;gap:46px;padding:20px 0 0 32px}
.card{width:297px;height:285px;background:linear-gradient(#fafafa,#dcdcdc);border-radius:24px;text-align:center;padding-top:11px}
.card-head{position:relative;margin:0 10px;height:60px;line-height:60px;border-radius:30px;background:linear-gradient(var(--gold-light),var(--gold));color:#fff;font-size:20px;text-transform:uppercase}
.card-head:after{content:"";position:absolute;left:50%;bottom:-10px;margin-left:-10px;border:10px solid transparent;border-bottom:0;border-top-color:var(--gold)}
.card p{font-size:14px;line-height:26px;color:#333;padding:24px 28px 0}
.price{font-size:24px;font-weight:700;color:var(--gold);margin-top:16px}
.partners-band{position:absolute;left:0;top:2150px;width:1200px;height:132px}
.countdown{position:absolute;left:0;top:2310px;width:1200px}
.timer{display:flex;justify-content:center;gap:35px;margin-top:26px}
.tbox{width:75px;height:79px;background:#111;border:2px solid #555;border-radius:4px;color:#fff;text-align:center}
.tbox b{display:block;font-size:36px;font-weight:500;line-height:52px}
.tbox span{font-size:10px;text-transform:uppercase}
.site-footer{position:absolute;left:0;top:2487px;width:1200px;height:184px;background:var(--darker);color:#fff}
.footer-nav{position:absolute;left:75px;top:52px;display:flex;gap:28px;font-size:12px;text-transform:uppercase}
.legal{position:absolute;left:75px;top:101px;font-size:11px;line-height:21px;color:#999}
.footer-brand{position:absolute;left:946px;top:58px;width:180px;text-align:center}
.footer-brand .brand-mark{background:#555;width:40px;height:40px}
.footer-brand .brand-name{color:#666}
</style>
</head>
<body>
<header class="site-header">
  <div class="follow"><span>FOLLOW US</span><i class="social"></i><i class="social"></i><i class="social"></i><i class="social"></i><i class="social"></i></div>
  <div class="brand"><div class="brand-mark"></div><div class="brand-name">Lantern Path</div></div>
  <a class="btn-gold header-cta">Register Now</a>
</header>
<nav class="main-nav">
  <a>Home</a><a>About</a><a>Conference Programs</a><a class="active">Register</a><a>Speaker Profiles</a><a>Regional Conferences</a><a>Contact</a>
</nav>
<div class="breadcrumb">Home &gt; <b>Registration</b></div>

<section class="logo-band">
  <div class="band-title"><span class="dot"></span><span>Network with<br><span class="gold">Executives</span></span></div>
  <div class="carousel"><span class="arrow">‹</span>
    <div class="items"><span class="partner">Northgate Alliance</span><span class="partner">Brightwell Media</span><span class="partner">Tempo Sound</span><span class="partner">Corelink Systems</span><span class="partner">Ridgeway Grill</span></div>
  <span class="arrow">›</span></div>
</section>

<section class="registration">
  <h2 class="section-title"><span class="dot"></span><span>Conference <span class="gold">Registration</span></span></h2>
  <div class="reg-text">
    <p>Your leadership conference registration includes complete access to all the different keynote speeches, panel discussions, group activities, workshop sessions, networking activities, reflection exercises, career opportunities, and other special events offered at the Lantern Path Leadership Experience.</p>
    <p>In addition to the amazing programs listed above, each participant will also receive a customized conference binder, business cards, certified leadership certificate, access to additional leadership and professional resources, and a free copy of an incredible leadership book that you can review with your leadership team after the conference is complete.</p>
    <p>To reserve your spot for this life changing leadership development conference, you can choose three different methods of payment</p>
  </div>
  <div class="reg-photo photo" role="img" aria-label="Speaker addressing a seated conference audience"></div>
</section>

<section class="roles">
  <div class="role"><div class="role-icon"><svg width="44" height="44" viewBox="0 0 44 44" fill="#222"><circle cx="22" cy="9" r="5"/><rect x="16" y="16" width="12" height="14" rx="3"/><rect x="12" y="32" width="20" height="8"/></svg></div><h3>Keynote Speaker</h3><p>Students will learn about more than twenty different leadership skills and qualities that leaders must possess in the 21st Century in order</p><a class="btn-dark">Read More</a></div>
  <div class="role"><div class="role-icon"><svg width="48" height="44" viewBox="0 0 48 44" fill="#222"><rect x="14" y="4" width="30" height="20" fill="none" stroke="#222" stroke-width="3"/><circle cx="8" cy="14" r="4"/><rect x="4" y="20" width="8" height="12"/><circle cx="18" cy="34" r="4"/><circle cx="30" cy="34" r="4"/><circle cx="42" cy="34" r="4"/></svg></div><h3>Workshop Presenters</h3><p>Students will learn about more than twenty different leadership skills and qualities that leaders must possess in the 21st Century in order</p><a class="btn-dark">Read More</a></div>
  <div class="role"><div class="role-icon"><svg width="48" height="44" viewBox="0 0 48 44" fill="#222"><circle cx="12" cy="10" r="5"/><circle cx="36" cy="10" r="5"/><rect x="6" y="17" width="12" height="14" rx="3"/><rect x="30" y="17" width="12" height="14" rx="3"/><rect x="14" y="26" width="20" height="4"/><circle cx="24" cy="36" r="4"/></svg></div><h3>Career Panelist Experts</h3><p>Students will learn about more than twenty different leadership skills and qualities that leaders must possess in the 21st Century in order</p><a class="btn-dark">Read More</a></div>
  <div class="role"><div class="role-icon"><svg width="48" height="44" viewBox="0 0 48 44" fill="#222"><circle cx="24" cy="9" r="5"/><circle cx="10" cy="13" r="4"/><circle cx="38" cy="13" r="4"/><rect x="18" y="16" width="12" height="22" rx="3"/><rect x="5" y="19" width="10" height="17" rx="3"/><rect x="33" y="19" width="10" height="17" rx="3"/></svg></div><h3>Leadership Executives</h3><p>Students will learn about more than twenty different leadership skills and qualities that leaders must possess in the 21st Century in order</p><a class="btn-dark">Read More</a></div>
</section>

<section class="logo-band schools">
  <div class="band-title"><span class="dot"></span><span>Connect with<br>other <span class="gold">Student<br>Leaders from</span></span></div>
  <div class="carousel"><span class="arrow">‹</span>
    <div class="items"><i class="badge"></i><i class="badge"></i><i class="badge"></i><i class="badge"></i><i class="badge"></i><i class="badge"></i></div>
  <span class="arrow">›</span></div>
</section>

<section class="register-cta">
  <div class="cta-photo" role="img" aria-label="Group of student leaders posing at the conference backdrop"></div>
  <a class="btn-gold cta-btn">Register Now</a>
  <p class="cta-text">For this transformational leadership experience that will connect you with an incredible diverse leadership network of students and professionals that provide you with the inspiration and leadership/professional skills needed to take your life to the next level!</p>
</section>

<section class="pricing">
  <h2 class="section-title"><span class="dot"></span><span>Conference <span class="gold">Pricing</span></span></h2>
  <div class="cards">
    <div class="card"><div class="card-head">Early Registration</div><p>If you register for the conference before October 15, 2016, your conference registration cost will be</p><div class="price">$150.00</div></div>
    <div class="card"><div class="card-head">Late Registration</div><p>If you register for the conference after October 15, 2016, your conference registration cost will be</p><div class="price">$175.00</div></div>
    <div class="card"><div class="card-head">Group Registration</div><p>If your campus is bringing 5 or more students, please email Maren Delacroix, our vice president of student engagement and logistics. She will assist you with the process and talk with you more about our group discount rate.</p></div>
  </div>
</section>

<section class="logo-band partners-band" style="background:var(--grey-band)">
  <div class="band-title"><span class="dot"></span><span>2015 Conference<br><span class="gold">Partners and<br>Supports</span></span></div>
  <div class="carousel"><span class="arrow">‹</span>
    <div class="items"><span class="partner">Sunvale Energy</span><span class="partner">Kestrel Motors</span><span class="partner">Greenleaf Coffee</span><span class="partner">Ember Cantina</span><span class="partner">Harbor Kitchen</span></div>
  <span class="arrow">›</span></div>
</section>

<section class="countdown">
  <h2 class="section-title"><span class="dot"></span><span>6th Annual <span class="gold">Conference Countdown</span></span></h2>
  <div class="timer">
    <div class="tbox"><b>0</b><span>Hours</span></div>
    <div class="tbox"><b>0</b><span>Minutes</span></div>
    <div class="tbox"><b>0</b><span>Seconds</span></div>
  </div>
</section>

<footer class="site-footer">
  <nav class="footer-nav"><span>Home</span><span>About</span><span>Conference</span><span>Register</span><span>Testimonials</span><span>Y Factor</span><span>Videos</span><span>Contact</span></nav>
  <div class="legal">Copyright © 2015. Company Name All Right Reserved<br>Privacy Policy &nbsp;|&nbsp; Term &amp; Conditions</div>
  <div class="footer-brand"><div class="brand-mark"></div><div class="brand-name">Lantern Path</div></div>
</footer>
</body>
</html>
```